Letterhead/Busines Cards for Harborview Psychiatry, PLLC - modern psychiatric practice
Harborview Psychiatry, PLLC
Professional
Gerald Matthis, MSN, APRN, PMHNP-BC
President
5812 Quailrun Lane
Lexington, KY 40509
tkwarden4@mailvista.example
please design leaving out black background

```html
<!DOCTYPE html>
<html lang="en">
<head>
<meta charset="utf-8">
<title>Harborview Psychiatry, PLLC – Business Card</title>
<link href="https://fonts.googleapis.com/css2?family=Open+Sans:wght@400;600&display=swap" rel="stylesheet">
<style>
  :root {
    --page-bg: #ecebe8;
    --gold-light: #f2b441;
    --gold-dark: #d98a1c;
    --card-white: #ffffff;
    --text-grey: #6d6e71;
    --divider: #9a9b9e;
    --icon-bg: #808285;
  }
  html, body {
    margin: 0;
    width: 1200px;
    height: 914px;
    overflow: hidden;
    background: var(--page-bg);
    font-family: "Open Sans", Arial, sans-serif;
  }
  .business-card {
    position: absolute;
    left: 75px;
    top: 157px;
    width: 1050px;
    height: 600px;
    box-sizing: border-box;
    padding: 24px;
    background: linear-gradient(135deg, var(--gold-light), var(--gold-dark));
    box-shadow: 0 10px 30px rgba(0,0,0,0.15);
  }
  .card-face {
    position: relative;
    width: 100%;
    height: 100%;
    background: var(--card-white);
  }
  .brand-block {
    position: absolute;
    left: 40px;
    top: 150px;
    width: 420px;
    text-align: center;
  }
  .brand-dot {
    display: block;
    width: 90px;
    height: 90px;
    margin: 0 auto 22px;
    border-radius: 50%;
    background: var(--gold-dark);
  }
  .brand-name {
    font-weight: 600;
    font-size: 34px;
    line-height: 1.25;
    color: var(--gold-dark);
    margin: 0;
  }
  .divider {
    position: absolute;
    left: 490px;
    top: 120px;
    width: 2px;
    height: 320px;
    background: var(--divider);
  }
  .contact-block {
    position: absolute;
    left: 520px;
    top: 118px;
    color: var(--text-grey);
  }
  .person-name, .person-credentials {
    margin: 0;
    font-size: 27px;
    line-height: 1.2;
    color: var(--gold-dark);
  }
  .person-title {
    margin: 2px 0 0;
    font-size: 22px;
    color: var(--text-grey);
  }
  .contact-list {
    list-style: none;
    margin: 34px 0 0;
    padding: 0;
    font-size: 19px;
  }
  .contact-list li {
    display: flex;
    align-items: center;
    height: 32px;
  }
  .contact-list .address-line {
    padding-left: 34px;
  }
  .contact-icon {
    width: 22px;
    height: 22px;
    margin-right: 12px;
    flex: none;
  }
</style>
</head>
<body>
  <section class="business-card">
    <div class="card-face">
      <div class="brand-block">
        <span class="brand-dot"></span>
        <p class="brand-name">Harborview Psychiatry, PLLC</p>
      </div>

      <div class="divider"></div>

      <div class="contact-block">
        <p class="person-name">Gerald Matthis,</p>
        <p class="person-credentials">MSN, APRN, PMHNP-BC</p>
        <p class="person-title">President</p>

        <ul class="contact-list">
          <li>
            <svg class="contact-icon" viewBox="0 0 22 22" aria-hidden="true">
              <circle cx="11" cy="11" r="11" fill="var(--icon-bg)"/>
              <path d="M11 5a4 4 0 0 0-4 4c0 3 4 8 4 8s4-5 4-8a4 4 0 0 0-4-4zm0 5.5a1.5 1.5 0 1 1 0-3 1.5 1.5 0 0 1 0 3z" fill="#fff"/>
            </svg>
            5812 Quailrun Lane
          </li>
          <li class="address-line">Lexington, KY 40509</li>
          <li>
            <svg class="contact-icon" viewBox="0 0 22 22" aria-hidden="true">
              <circle cx="11" cy="11" r="11" fill="var(--icon-bg)"/>
              <path d="M8 5.5l2 2.5-1.2 1.5a7 7 0 0 0 3.7 3.7L14 12l2.5 2-1.3 2A8 8 0 0 1 6 6.8z" fill="#fff"/>
            </svg>
            (859) 555-0142
          </li>
          <li>
            <svg class="contact-icon" viewBox="0 0 22 22" aria-hidden="true">
              <circle cx="11" cy="11" r="11" fill="var(--icon-bg)"/>
              <rect x="7" y="5" width="8" height="12" rx="1.5" fill="#fff"/>
              <rect x="8.5" y="7" width="5" height="7" fill="var(--icon-bg)"/>
            </svg>
            (859) 555-0187
          </li>
          <li>
            <svg class="contact-icon" viewBox="0 0 22 22" aria-hidden="true">
              <circle cx="11" cy="11" r="11" fill="var(--icon-bg)"/>
              <rect x="5.5" y="7" width="11" height="8" fill="#fff"/>
              <path d="M5.5 7l5.5 4.5L16.5 7" fill="none" stroke="var(--icon-bg)" stroke-width="1.2"/>
            </svg>
            tkwarden4@mailvista.example
          </li>
          <li>
            <svg class="contact-icon" viewBox="0 0 22 22" aria-hidden="true">
              <circle cx="11" cy="11" r="11" fill="var(--icon-bg)"/>
              <circle cx="11" cy="11" r="5.5" fill="none" stroke="#fff" stroke-width="1.3"/>
              <path d="M5.5 11h11M11 5.5c-2.5 3-2.5 8 0 11M11 5.5c2.5 3 2.5 8 0 11" fill="none" stroke="#fff" stroke-width="1.1"/>
            </svg>
            www.harborviewpsych.example
          </li>
        </ul>
      </div>
    </div>
  </section>
</body>
</html>
```